Bref créative
New Corporate Website - Blue Falcons
Blue Falcons - Marketing & Lead Generation
Marketing
Does not yet exist
Blue Falcons is a new Marketing and Sales Lead generation agency specializing in helping companies analyze, pursue and close sales opportunities generated via the Internet. We provide access to our exclusive Blue Falcon Striker platform for capturing and pursing sales opportunities generated via the online platform.
I'd like to showcase a lot of red on this website. This is a new website for a new company we are starting.
The website is to feature both our online web software as well as our consulting services.
High Tech
Red (#aa0000)
Grey (#cccccc)
Verdana
Century Gothic
top
http://www.vortelix.com
http://www.brinaxo.com/en
http://www.quombrel.com
The page should include links for
Navigation
- About Blue Falcons
- Services & Solutions
- Results
- News & Announcements
- Contact Us
Also, an area for current customer's to login
please incorporate the logo of the man riding the horse backwards.

```html
<!DOCTYPE html>
<html lang="en">
<head>
<meta charset="utf-8">
<title>Blue Falcons - Marketing &amp; Lead Generation</title>
<link rel="stylesheet" href="https://fonts.googleapis.com/css2?family=Arimo:wght@400;700&display=swap">
<style>
:root{
  --red:#aa0000;
  --red-bright:#c40000;
  --grey:#cccccc;
  --backdrop:#d9dadb;
  --white:#ffffff;
  --text-muted:#9a9a9a;
  --ink:#333333;
}
*{box-sizing:border-box;margin:0;padding:0}
html,body{width:1200px;height:1059px;overflow:hidden}
body{
  background:radial-gradient(circle at 30% 40%,#eceded 0,#d3d4d5 60%,#c4c5c6 100%);
  font-family:"Arimo",Verdana,sans-serif;
  position:relative;
}
.page{position:absolute;left:157px;top:0;width:877px;height:1029px;background:var(--white)}
.site-header{position:absolute;left:0;top:0;width:877px;height:100px;background:var(--red)}
.brand{position:absolute;left:14px;top:8px;color:var(--white);font-size:58px;font-weight:400;letter-spacing:-0.5px}
.account{position:absolute;right:26px;top:6px;display:flex;gap:36px}
.account a{color:var(--white);font-size:14px;text-decoration:none}
.main-nav{position:absolute;left:0;top:106px;width:877px;height:48px;display:flex;border-top:1px solid var(--grey);border-bottom:1px solid var(--grey)}
.main-nav a{display:flex;align-items:center;justify-content:center;color:var(--red);font-size:14px;text-decoration:none;border-right:1px solid var(--grey);height:100%}
.main-nav a.active{background:var(--red);color:var(--white)}
.main-nav a:last-child{border-right:none}
.hero-map{position:absolute;left:14px;top:172px;width:376px;height:290px;background:radial-gradient(ellipse at 50% 50%,#d42a1a 0,#b31208 45%,#ffffff 72%)}
.news{position:absolute;left:400px;top:166px;width:463px;height:298px;background:var(--red);border-radius:8px;padding:8px 10px}
.news h2{color:var(--white);font-size:36px;font-weight:700;line-height:42px;padding-bottom:4px;border-bottom:2px solid var(--white);margin-bottom:8px}
.news-item{display:flex;gap:8px;margin-bottom:10px;color:var(--white);font-size:13px;line-height:17px}
.news-item svg{flex:none;margin-top:2px}
.news-item time{display:block;font-size:12px;margin-bottom:6px}
.section-title{position:absolute;left:0;top:520px;width:877px;height:58px;background:var(--red);color:var(--white);font-size:41px;line-height:58px;padding-left:8px;font-weight:400}
.intro{position:absolute;left:6px;top:584px;width:570px;color:var(--text-muted);font-size:11px;line-height:16.5px}
.photo{position:absolute}
.photo-history{left:592px;top:586px;width:280px;height:115px;background:linear-gradient(135deg,#c99a62,#8a4f2a 55%,#d2b07c)}
.photo-team{left:6px;top:829px;width:217px;height:142px;background:radial-gradient(circle at 40% 45%,#c02018 0,#333 35%,#e9e9e9 75%)}
.photo-riders{left:243px;top:829px;width:217px;height:142px;background:linear-gradient(180deg,#a8c3de 0,#7f8f9a 45%,#6d6a4a 100%)}
.consult{position:absolute;left:592px;top:706px;width:280px}
.consult h3{display:inline-block;background:var(--red);color:var(--white);font-size:30px;font-weight:400;padding:2px 8px;border-radius:4px;margin-bottom:6px}
.field{background:var(--red);color:var(--white);font-size:14px;border-radius:5px;height:30px;padding:6px 6px;margin-bottom:8px}
.field.tall{height:64px}
.submit{display:block;margin-left:auto;margin-right:10px;background:var(--red);color:var(--white);border:none;font-family:inherit;font-size:14px;padding:4px 10px;border-radius:3px}
.site-footer{position:absolute;left:0;top:980px;width:877px;height:49px;background:var(--red);display:flex;align-items:center;justify-content:space-between;padding:0 8px;color:var(--white);font-size:13px}
.site-footer nav{display:flex;gap:12px}
.site-footer a{color:var(--white);text-decoration:none}
</style>
</head>
<body>
<div class="page">
  <header class="site-header">
    <div class="brand">Blue Falcons</div>
    <div class="account"><a href="#">LOG IN</a><a href="#">SIGN UP</a></div>
  </header>
  <nav class="main-nav">
    <a class="active" href="#" style="width:163px">About Blue Falcons</a>
    <a href="#" style="width:188px">Services &amp; Solutions</a>
    <a href="#" style="width:154px">Results</a>
    <a href="#" style="width:232px">News &amp; Announcements</a>
    <a href="#" style="width:140px">Contact Us</a>
  </nav>

  <div class="hero-map" role="img" aria-label="Red world map with silhouettes of business people standing on it"></div>

  <aside class="news">
    <h2>News &amp; Announcements</h2>
    <div class="news-item">
      <svg width="22" height="22" viewBox="0 0 22 22"><rect x="1" y="3" width="20" height="18" fill="#fff"/><rect x="1" y="3" width="20" height="5" fill="#ddd"/><path d="M5 1v5M17 1v5" stroke="#fff" stroke-width="2"/></svg>
      <div><time>21-july-2011</time>Contrary to popular belief, Lorem Ipsum is not simply random text.<br>It has roots in a piece of classical Latin literature from 45 BC</div>
    </div>
    <div class="news-item">
      <svg width="22" height="22" viewBox="0 0 22 22"><rect x="1" y="3" width="20" height="18" fill="#fff"/><rect x="1" y="3" width="20" height="5" fill="#ddd"/><path d="M5 1v5M17 1v5" stroke="#fff" stroke-width="2"/></svg>
      <div><time>21-july-2011</time>Contrary to popular belief, Lorem Ipsum is not simply random text.<br>It has roots in a piece of classical Latin literature from 45 BC</div>
    </div>
    <div class="news-item">
      <svg width="22" height="22" viewBox="0 0 22 22"><rect x="1" y="3" width="20" height="18" fill="#fff"/><rect x="1" y="3" width="20" height="5" fill="#ddd"/><path d="M5 1v5M17 1v5" stroke="#fff" stroke-width="2"/></svg>
      <div><time>21-july-2011</time>Contrary to popular belief, Lorem Ipsum is not simply random text.<br>It has roots in a piece of classical Latin literature from 45 BC</div>
    </div>
  </aside>

  <h1 class="section-title">Blue Falcons - Marketing &amp; Lead Generation</h1>

  <p class="intro">Lorem Ipsum is simply dummy text of the printing and typesetting industry. Lorem Ipsum has been the industry's standard dummy text ever since the 1500s, when an unknown printer took a galley of type and scrambled it to make a type specimen book. Lorem Ipsum is simply dummy text of the printing and typesetting industry. Lorem Ipsum has been the industry's standard dummy text ever since the 1500s, when an unknown printer took a galley of type and scrambled it to make a type specimen book. Lorem Ipsum is simply dummy text of the printing and typesetting industry. Lorem Ipsum has been the industry's standard dummy text ever since the 1500s, when an unknown printer took a galley of type and scrambled it to make a type specimen book. Lorem Ipsum is simply dummy text of the printing and typesetting industry. Lorem Ipsum has been the industry's standard dummy text ever since the 1500s, when an unknown printer took a galley of type and scrambled it to make a type specimen book.</p>

  <div class="photo photo-history" role="img" aria-label="Historic painting of horse riders in warm earth tones"></div>
  <div class="photo photo-team" role="img" aria-label="Red game piece leading a group of black pieces"></div>
  <div class="photo photo-riders" role="img" aria-label="Riders on horseback in colourful dress on open grassland"></div>

  <form class="consult">
    <h3>Free counsulting</h3>
    <div class="field">NAME</div>
    <div class="field">EMAIL</div>
    <div class="field">ADDRESSED</div>
    <div class="field tall">COMPANY</div>
    <button class="submit" type="submit">SUBMIT</button>
  </form>

  <footer class="site-footer">
    <nav>
      <a href="#">About Blue Falcons</a>
      <a href="#">Services &amp; Solutions</a>
      <a href="#">Results</a>
      <a href="#">News &amp; Announcements</a>
      <a href="#">Contact Us</a>
    </nav>
    <span>©Copyright 2011 Blue Falcons</span>
  </footer>
</div>
</body>
</html>
```